Bridge of Kites is an art based humanitarian project which takes 'at risk' and 'disadvantaged' youths on a life changing humanitarian journey.

Bridge of Kites is based in Forster, coastal NSW, however is hoping to expand throughout Australia.

I have a logo and would like it to be predominantly used on the business card.

Bridge of Kites uses art as the catalyst to bring together the young adults from across countries. The aim is to help each other heal their hearts through giving.

Could you please add the following to the cards under Bridge of Kites::

Changing lives through humanity and art.

Target Market(s)

The target audience will be companies or businesses interested in supporting Bridge of Kites. Also, School principals and teachers.

It may help to watch the following trailer about a documentary being made on Bridge of Kites: www.fundvessel.org/project/48213

Industry/Entity Type

Business

Contact Information for Business Card

Bridge of Kites
Mavis Threlkeld
Founder

P O BOX 7, KELWYN BAY, NSW, 2419
AUSTRALIA
PH 0471382956

kite_bridge41@quillpost.net

Logo Text

Bridge of Kites

Requirements
Must have
• Must have attached Bridge of Kites logo. (I am not sure if this has uploaded on this site????)
Nice to have
• Colour

```html
<!DOCTYPE html>
<html lang="en">
<head>
<meta charset="utf-8">
<title>Bridge of Kites – Business Cards</title>
<link href="https://fonts.googleapis.com/css2?family=Questrial&display=swap" rel="stylesheet">
<style>
  :root {
    --backdrop: #e9e4dc;
    --card-dark: #1c1c1c;
    --card-dark-band: #262626;
    --card-dark-line: #3a3a3a;
    --card-light: #ffffff;
    --teal: #3aa8b8;
    --teal-soft: #7fbcc4;
    --coral: #e8506a;
  }
  * { box-sizing: border-box; margin: 0; padding: 0; }
  html, body { width: 1200px; height: 1000px; overflow: hidden; }
  body {
    position: relative;
    background: var(--backdrop);
    font-family: "Questrial", sans-serif;
  }
  .card { position: absolute; overflow: hidden; }

  .card-front {
    left: 263px; top: 92px; width: 697px; height: 395px;
    background: var(--card-dark);
    border-radius: 56px 0 56px 0;
  }
  .card-front .band-top {
    position: absolute; left: 0; top: 0; width: 100%; height: 66px;
    background: linear-gradient(#3a3a3a, var(--card-dark-band));
    border-bottom: 2px solid var(--card-dark-line);
  }
  .card-front .band-bottom {
    position: absolute; left: 0; bottom: 0; width: 100%; height: 72px;
    background: var(--card-dark-band);
    border-top: 2px solid var(--card-dark-line);
  }
  .brand {
    position: absolute;
    display: flex; align-items: center; gap: 14px;
    color: var(--teal);
    white-space: nowrap;
  }
  .brand-dot {
    flex: none; border-radius: 50%;
    background: var(--coral);
  }
  .card-front .brand {
    left: 0; right: 0; top: 172px; justify-content: center;
    font-size: 52px; line-height: 1;
  }
  .card-front .brand-dot { width: 34px; height: 34px; }

  .card-back {
    top: 603px; width: 547px; height: 310px;
    background: var(--card-light);
    border-radius: 0 60px 0 60px;
  }
  .card-back.is-left { left: 35px; }
  .card-back.is-right { left: 627px; }

  .card-back .brand { line-height: 1; gap: 10px; }
  .card-back.is-left .brand { left: 30px; top: 62px; font-size: 30px; }
  .card-back.is-right .brand { left: 18px; top: 72px; font-size: 40px; }
  .card-back.is-left .brand-dot { width: 22px; height: 22px; }
  .card-back.is-right .brand-dot { width: 28px; height: 28px; }

  .contact {
    position: absolute; left: 298px; top: 190px;
    color: var(--teal);
  }
  .card-back.is-right .contact { left: 308px; }
  .contact-name { font-size: 21px; line-height: 1; }
  .contact-role {
    font-size: 9px; letter-spacing: 4.5px; color: var(--teal-soft);
    margin: 3px 0 0 64px;
  }
  .contact-lines {
    list-style: none; margin-top: 14px;
    font-size: 11px; line-height: 14px;
  }
</style>
</head>
<body>

  <section class="card card-front" aria-label="Card front">
    <div class="band-top"></div>
    <div class="band-bottom"></div>
    <div class="brand"><span class="brand-dot"></span>Bridge of Kites</div>
  </section>

  <section class="card card-back is-left" aria-label="Card back, compact logo">
    <div class="brand"><span class="brand-dot"></span>Bridge of Kites</div>
    <div class="contact">
      <p class="contact-name">Mavis Threlkeld</p>
      <p class="contact-role">FOUNDER</p>
      <ul class="contact-lines">
        <li>P O BOX 7, KELWYN BAY, NSW, 2419 AUSTRALIA</li>
        <li>Ph: 0471382956</li>
        <li>E: kite_bridge41@quillpost.net</li>
      </ul>
    </div>
  </section>

  <section class="card card-back is-right" aria-label="Card back, large logo">
    <div class="brand"><span class="brand-dot"></span>Bridge of Kites</div>
    <div class="contact">
      <p class="contact-name">Mavis Threlkeld</p>
      <p class="contact-role">FOUNDER</p>
      <ul class="contact-lines">
        <li>P O BOX 7, KELWYN BAY, NSW, 2419 AUSTRALIA</li>
        <li>Ph: 0471382956</li>
        <li>E: kite_bridge41@quillpost.net</li>
      </ul>
    </div>
  </section>

</body>
</html>
```